New Plumbing Company

We are looking for a smart and creative business card design for our new plumbing company. We are looking for creativity and originality in our business cards.

Industry/Entity Type

Plumbing

Contact Information for Business Card

Crestline Plumbing
Peter Halvane
Managing Director
Telephone Number : 0481529604
Email : service@crestlineplumbing.com.au
Website : www.crestlineplumbing.com.au
Lic. 508264K

Colors
0692cd
33a6d7
000000

Requirements
Must have
• I want the business card to be designed on a black background using the blue tones i have selected as seen in the company logo.

```html
<!DOCTYPE html>
<html lang="en">
<head>
<meta charset="utf-8">
<title>Crestline Plumbing — Business Cards</title>
<link href="https://fonts.googleapis.com/css2?family=Questrial&family=Montserrat:wght@700&display=swap" rel="stylesheet">
<style>
  :root {
    --blue-deep: #0692cd;
    --blue-light: #33a6d7;
    --black: #000000;
    --charcoal: #2a2a2a;
    --graphite: #151515;
    --silver: #c9ccd0;
    --white: #ffffff;
    --page: #ecebe8;
  }
  * { box-sizing: border-box; margin: 0; padding: 0; }
  html, body { width: 1200px; height: 1200px; overflow: hidden; }
  body {
    background: var(--page);
    font-family: "Questrial", "Century Gothic", sans-serif;
    display: flex; flex-direction: column; align-items: center; justify-content: center;
    gap: 50px;
  }
  .card {
    position: relative;
    width: 860px; height: 526px;
    background: linear-gradient(180deg, var(--black) 0%, var(--graphite) 60%, var(--charcoal) 100%);
    box-shadow: 0 10px 30px rgba(0,0,0,.25);
    overflow: hidden;
    color: var(--white);
  }
  .rule {
    position: absolute; left: 0; right: 0; height: 5px;
    background: linear-gradient(90deg, #8c9095, var(--silver) 50%, #8c9095);
  }
  /* front */
  .front-band {
    position: absolute; left: 0; right: 0; top: 95px; height: 235px;
    background: linear-gradient(100deg, var(--blue-deep) 0%, var(--blue-light) 55%, var(--blue-deep) 100%);
  }
  .brand {
    position: absolute; display: flex; align-items: center; gap: 22px;
  }
  .brand-mark {
    width: 96px; height: 96px; border-radius: 50%;
    border: 6px solid var(--white);
  }
  .brand-name {
    font-size: 64px; line-height: 1; letter-spacing: 1px; color: var(--white);
  }
  .front .brand { left: 140px; top: 164px; }
  .website {
    position: absolute; left: 0; right: 0; top: 390px;
    text-align: center; font-size: 25px; letter-spacing: 9px; color: var(--white);
  }
  /* back */
  .back-photo {
    position: absolute; left: 0; right: 0; top: 0; height: 255px;
    background: linear-gradient(180deg, #1b1b1b 0%, #2c2c2c 50%, #141414 100%);
  }
  .back .brand { left: 180px; top: 80px; }
  .back .brand-mark { border-color: var(--blue-deep); }
  .contact { position: absolute; left: 60px; top: 300px; }
  .contact-name {
    font-family: "Montserrat", sans-serif; font-weight: 700;
    font-size: 19px; letter-spacing: 1.5px; text-transform: uppercase;
  }
  .contact-role { font-size: 21px; margin-top: 4px; }
  .contact-divider { width: 360px; height: 2px; background: var(--blue-deep); margin: 10px 0 14px; }
  .contact-list { list-style: none; font-size: 20px; line-height: 33px; }
  .contact-list li { display: flex; align-items: center; gap: 14px; }
  .contact-list svg { width: 18px; height: 18px; fill: var(--white); flex: none; }
  .address {
    position: absolute; right: 60px; bottom: 50px;
    text-align: right; font-size: 22px; line-height: 31px; letter-spacing: 1px;
  }
</style>
</head>
<body>

<section class="card front">
  <div class="rule" style="top:90px"></div>
  <div class="front-band" role="img" aria-label="Blue-toned photograph of a plumber working on pipework"></div>
  <div class="rule" style="top:330px"></div>
  <div class="brand">
    <span class="brand-mark"></span>
    <span class="brand-name">Crestline Plumbing</span>
  </div>
  <p class="website">www.crestlineplumbing.com.au</p>
</section>

<section class="card back">
  <div class="back-photo" role="img" aria-label="Dark monochrome photograph of chrome plumbing fittings"></div>
  <div class="rule" style="top:255px"></div>
  <div class="brand">
    <span class="brand-mark"></span>
    <span class="brand-name">Crestline Plumbing</span>
  </div>

  <div class="contact">
    <p class="contact-name">Peter Halvane</p>
    <p class="contact-role">Managing Director</p>
    <div class="contact-divider"></div>
    <ul class="contact-list">
      <li>
        <svg viewBox="0 0 24 24" aria-hidden="true"><path d="M6.6 10.8a15.1 15.1 0 0 0 6.6 6.6l2.2-2.2c.3-.3.7-.4 1-.2 1.1.4 2.3.6 3.6.6.6 0 1 .4 1 1V20c0 .6-.4 1-1 1A17 17 0 0 1 3 4c0-.6.4-1 1-1h3.5c.6 0 1 .4 1 1 0 1.3.2 2.5.6 3.6.1.3 0 .7-.2 1z"/></svg>
        0481529604
      </li>
      <li>
        <svg viewBox="0 0 24 24" aria-hidden="true"><path d="M2 5h20v14H2zm2 2v.5l8 5 8-5V7l-8 5z"/></svg>
        service@crestlineplumbing.com.au
      </li>
      <li>
        <svg viewBox="0 0 24 24" aria-hidden="true"><path d="M5 2h10l4 4v16H5zm2 6v2h10V8zm0 4v2h10v-2zm0 4v2h7v-2z"/></svg>
        Lic. 508264K
      </li>
    </ul>
  </div>

  <address class="address" style="font-style:normal">
    Harbour House,<br>
    14 Keel Street,<br>
    London, SE9 4PW
  </address>
</section>

</body>
</html>
```